Need label design for car cleaning spray bottle, big opportunity for repeat work

This is the first label design for a large assortment of car cleaning products. This design will be vital as it will set the design style for the remaining products. There is large opportunity for repeat work to the winning designer. For this first product we plan to call it "Interior Cleaner". We have the template label which we have attached to the project. The product is geared towards the market of Volmara car owners, and our logo also utilizes a similar font to what Volmara's company font uses.

We are looking to only update the design/format of the label. We will keep all text the same or modify it once the design is final. We will need to use our brand logo (attached).

We are looking for a minimalistic style design. Currently the label reads horizontally but we have noticed that the most successful brands that sell online have a vertical style design. We have attached some examples of brands such as "Gleam Bastion" and "Pivlo" which sell primarily on shopvendrix.com and have tens of thousands of reviews. We'd like to try and copy this label format as it seems very successful for these brands.

We are big fans of the minimal style that the brand "AutoZell" uses. Their label design emphasizes the name of the particular product in black text on a white background. The remainder of the label is color coded, and all of their products have a different color code while following the same diagonal design style. See attached examples.

So that being said, we would like to combine these 2 concepts, vertical alignment style with the minimalistic label design.

We are thinking of making the entire label white, and having an accent color like 1 large stripe that goes across the bottle, it would be an iconic part of the design as we will repeat this design across multiple products, similar to the AutoZell brand bundle example we attached. This specific product will be pink liquid (as you can tell the accent color is pink on the label).

We'd like to add a dynamic QR code (can use placeholder) on the label so customers can be directed to our website easily or any other page we choose in the future. We will also need a UPC barcode label (can use placeholder)

Target Market(s)

Volmara car owners

Industry/Entity Type

Car Detailing Products

Font styles to use
Sans Serif

Colors
E54698
E96AAD
F1A4CE
F9D9EA
FCEFF6

Requirements
Must have
• minimalistic design
Should not have
• no designs similar to brands like polish crew, dravonels, or any older brands in the category

```html
<!DOCTYPE html>
<html lang="en">
<head>
<meta charset="utf-8">
<title>Velnari Interior Cleaner Label</title>
<link rel="stylesheet" href="https://fonts.googleapis.com/css2?family=Montserrat:wght@300;500;700;800&family=Oswald:wght@600;700&display=swap">
<style>
  :root {
    --pink-deep: #e54698;
    --pink: #e96aad;
    --pink-soft: #f1a4ce;
    --pink-pale: #f9d9ea;
    --pink-mist: #fceff6;
    --ink: #111111;
    --paper: #ffffff;
    --backdrop: #e6e6e6;
  }
  * { margin: 0; padding: 0; box-sizing: border-box; }
  html, body {
    width: 1200px; height: 999px; overflow: hidden;
    background: var(--backdrop);
  }
  .canvas {
    position: relative; width: 1200px; height: 999px;
  }
  .label {
    position: absolute; left: 340px; top: 60px;
    width: 520px; height: 880px;
    background: var(--paper);
    overflow: hidden;
    box-shadow: 0 6px 24px rgba(0,0,0,0.08);
  }
  .accent-stripe {
    position: absolute; left: 0; top: 40px;
    width: 100%; height: 130px;
    background: linear-gradient(90deg, var(--pink-deep) 0%, var(--pink) 55%, var(--pink-deep) 100%);
  }
  .label-copy {
    position: absolute;
    width: 680px; height: 440px;
    left: -80px; top: 300px;
    transform: rotate(-90deg);
    padding: 30px 20px 20px 20px;
    display: flex; flex-direction: column;
  }
  .brand-name {
    font-family: "Montserrat", sans-serif;
    font-weight: 300;
    font-size: 92px;
    letter-spacing: 20px;
    line-height: 1;
    color: var(--ink);
    white-space: nowrap;
  }
  .brand-name sup {
    font-size: 22px; font-weight: 500; letter-spacing: 0;
    vertical-align: top; position: relative; top: -4px;
  }
  .product-name {
    margin-top: 14px;
    font-family: "Oswald", sans-serif;
    font-weight: 700;
    font-size: 62px;
    line-height: 1;
    letter-spacing: -1px;
    color: var(--ink);
    text-transform: uppercase;
    white-space: nowrap;
  }
  .divider {
    margin-top: 16px;
    height: 2px; width: 100%;
    background: var(--pink-deep);
  }
  .feature-badges {
    margin-top: 20px;
    display: flex; gap: 18px;
    padding-left: 40px;
  }
  .badge {
    width: 108px; height: 108px; border-radius: 50%;
    background: var(--ink);
    border: 4px solid var(--pink-deep);
    color: var(--paper);
    display: flex; flex-direction: column; align-items: center; justify-content: center;
    font-family: "Montserrat", sans-serif;
    text-transform: uppercase;
    text-align: center;
    line-height: 1.05;
  }
  .badge .big { font-weight: 800; font-size: 19px; }
  .badge .small { font-weight: 500; font-size: 11px; letter-spacing: 0.5px; }
</style>
</head>
<body>
<div class="canvas">
  <div class="label">
    <div class="accent-stripe"></div>
    <div class="label-copy">
      <div class="brand-name">VELNARI<sup>®</sup></div>
      <div class="product-name">Interior Cleaner</div>
      <div class="divider"></div>
      <div class="feature-badges">
        <div class="badge">
          <span class="small">Removes</span>
          <span class="small">Grease</span>
          <span class="big">Grime</span>
          <span class="big">&amp;Dirt</span>
        </div>
        <div class="badge">
          <span class="small">Interior</span>
          <span class="big">And</span>
          <span class="small">Exterior</span>
        </div>
        <div class="badge">
          <span class="big">Non</span>
          <span class="big">Acidic</span>
          <span class="small">Formula</span>
        </div>
      </div>
    </div>
  </div>
</div>
</body>
</html>
```